Quimby's Yard & Garden Center Business Card Update

I need an updated Business card design for my Lawn and Garden Center. We do Landscaping installs, Lawn Mowing, Snow Removal and also have a Garden Center Retail Division. I uploaded a few of our previous business cards to give an idea of what we are starting with. The main goal of this update is to simplify and modernize the business card, not all of the services that are on the previous cards has to be on the new one but I would still like to highlight our main services. There is also a sample of our logo that Can be used in the design.

Industry/Entity Type

Landscaping

Contact Information for Business Card

Morris Quimby
Morris@Quimbysyardandgarden.example
Business (555) 201-7784
Cell (555) 318-6092

Colors

Designer to choose colors to be used in the design.

Requirements
Must have
• Services Provided :
• Landscaping
• Lawn Maintenance
• Snow Removal
• Garden Center

```html
<!DOCTYPE html>
<html lang="en">
<head>
<meta charset="utf-8">
<title>Quimby's Yard &amp; Garden Center – Business Card</title>
<link href="https://fonts.googleapis.com/css2?family=Josefin+Sans:wght@400;600;700&family=Arimo:wght@700&display=swap" rel="stylesheet">
<style>
  :root {
    --page: #6f7073;
    --leaf: #2f5e27;
    --leaf-soft: #9fb694;
    --ink: #141414;
    --photo-top: #dfe8e2;
    --photo-mid: #b9c9ad;
    --photo-low: #8fa283;
    --veil: rgba(255,255,255,0.42);
  }
  * { box-sizing: border-box; margin: 0; padding: 0; }
  html, body { width: 1200px; height: 965px; overflow: hidden; }
  body {
    background: var(--page);
    position: relative;
    font-family: "Josefin Sans", sans-serif;
    color: var(--ink);
  }
  .card {
    position: absolute;
    left: 281px;
    width: 639px;
    height: 372px;
    border-radius: 16px;
    overflow: hidden;
  }
  .card--front { top: 74px; }
  .card--back { top: 518px; }
  .card__photo {
    position: absolute; inset: 0;
    background: linear-gradient(180deg, var(--photo-top) 0%, var(--photo-mid) 45%, var(--photo-low) 100%);
  }
  .card__veil { position: absolute; inset: 0; background: var(--veil); }
  .brand {
    position: absolute;
    display: flex; align-items: center; gap: 8px;
    font-family: "Josefin Sans", sans-serif;
    font-weight: 700;
    color: var(--leaf);
  }
  .brand__dot { width: 16px; height: 16px; border-radius: 50%; background: var(--leaf); }
  .card--front .brand { left: 38px; top: 48px; font-size: 34px; }
  .card--back .brand { right: 36px; top: 52px; font-size: 44px; }
  .brand-ghost {
    position: absolute;
    font-family: "Josefin Sans", sans-serif;
    font-weight: 700;
    color: var(--leaf-soft);
    opacity: 0.55;
    white-space: nowrap;
  }
  .card--front .brand-ghost { left: 300px; top: 168px; font-size: 72px; }
  .card--back .brand-ghost { left: 16px; top: 70px; font-size: 76px; }
  .contact { position: absolute; left: 38px; top: 124px; }
  .contact__name { font-weight: 700; font-size: 24px; letter-spacing: 1px; color: var(--leaf); line-height: 28px; }
  .contact__role { font-size: 19px; line-height: 24px; }
  .contact__address { margin-top: 14px; font-size: 17px; line-height: 25px; letter-spacing: 0.6px; }
  .contact__lines { margin-top: 18px; list-style: none; }
  .contact__lines li { display: flex; align-items: center; gap: 8px; font-size: 17px; letter-spacing: 0.8px; height: 31px; }
  .contact__lines svg { width: 22px; height: 18px; fill: var(--leaf); flex: none; }
  .services {
    position: absolute; right: 40px; top: 158px;
    list-style: none; text-align: right;
    font-family: "Arimo", sans-serif; font-weight: 700;
    font-size: 23px; letter-spacing: 1px; line-height: 34px;
  }
  .services li::after {
    content: ""; display: inline-block;
    width: 6px; height: 6px; border-radius: 50%;
    background: var(--leaf); margin-left: 4px; vertical-align: 1px;
  }
</style>
</head>
<body>
  <section class="card card--front">
    <div class="card__photo" role="img" aria-label="Greenhouse interior with potted ornamental grasses and plants on benches"></div>
    <div class="card__veil"></div>
    <div class="brand-ghost" aria-hidden="true">Quimby's</div>
    <div class="brand"><span class="brand__dot"></span>Quimby's</div>
    <div class="contact">
      <p class="contact__name">MORRIS QUIMBY</p>
      <p class="contact__role">Founder/CEO</p>
      <p class="contact__address">11820 County Road<br>K 55501 Millbrook Ohio</p>
      <ul class="contact__lines">
        <li><svg viewBox="0 0 22 18"><path d="M1 6c0-3 4-5 10-5s10 2 10 5v2h-5V6H6v2H1z"/><path d="M5 9h12l2 8H3z"/></svg>(555) 201-7784</li>
        <li><svg viewBox="0 0 22 18"><path d="M7 0h8a1.5 1.5 0 0 1 1.5 1.5v15A1.5 1.5 0 0 1 15 18H7a1.5 1.5 0 0 1-1.5-1.5v-15A1.5 1.5 0 0 1 7 0zm0.5 2v12h7V2zm3.5 13a1 1 0 1 0 0 2 1 1 0 0 0 0-2z"/></svg>(555) 318-6092</li>
        <li><svg viewBox="0 0 22 18"><path d="M1 3h20v1L11 10 1 4z"/><path d="M1 6l10 6 10-6v10H1z"/></svg>Morris@Quimbysyardandgarden.example</li>
      </ul>
    </div>
  </section>

  <section class="card card--back">
    <div class="card__photo" role="img" aria-label="Greenhouse garden center with rows of potted shrubs and flowers"></div>
    <div class="card__veil"></div>
    <div class="brand-ghost" aria-hidden="true">Quimby's</div>
    <div class="brand"><span class="brand__dot"></span>Quimby's</div>
    <ul class="services">
      <li>Landscaping installs</li>
      <li>Lawn Mowing</li>
      <li>Snow Removal</li>
      <li>and also have a</li>
      <li>Garden Center</li>
      <li>Retail Division</li>
    </ul>
  </section>
</body>
</html>
```